Just to be clear - I have the domain and the wordpress site (which is messy). I need someone to help me complete a simple blog design and then go into the existing wordpress site, and get rid of all the existing rubbish and set up the templates please. If we progress with design can we please be clear about additional costs upfront which, of course, I appreciate is the case.

Need a lifestyle blog. It is called brightyearsahead.com. Aimed at the older woman but needs to look fresh and young, not old fashioned. Navigation will be Home, Fashion, Feelings, Fitness, Contact. I have a logo but not sure it will work at the moment so happy with stylised words.Will have social media links.

Need homepage (not overly long) to have a main slider for pics/videos. Then the three category boxes underneath linking through to 2nd level pages containing blogs for that category and then the actual blog page. Happy to be led by expertise if this is not gonna work.

Am really looking for something clean and fresh like a Marvette type approach to be honest.

If you need any further direction please just ask - once design chosen I am looking to move quickly.

Thank you so much for looking at this brief

Target Market(s)

Women, 40 - 60 age group but with a younger outlook

Colors

Requirements
Must have
• Reflect youth, fun, bright
• Lift easily into a wordpress format
Should not have
• Old, staid, frumpy,dark

```html
<!DOCTYPE html>
<html lang="en">
<head>
<meta charset="utf-8">
<title>brightyearsahead.com</title>
<link href="https://fonts.googleapis.com/css2?family=Cinzel:wght@400;600;700&family=Raleway:wght@400;500&display=swap" rel="stylesheet">
<style>
:root{
  --olive:#a4a03e;
  --sage:#687869;
  --sage-dark:#4f5d52;
  --ink:#1f2420;
  --muted:#777;
  --white:#fff;
  --cream:#f6f5ec;
  --line:#d6d6d6;
}
*{margin:0;padding:0;box-sizing:border-box}
html,body{width:674px;height:1200px;overflow:hidden;background:var(--white)}
body{position:relative;font-family:"Raleway",Arial,sans-serif;color:var(--ink)}
.abs{position:absolute}
.top-rule{left:0;top:0;width:674px;height:2px;background:var(--sage-dark)}
.logo{left:66px;top:17px;font-family:"Cinzel",serif;font-size:20px;color:var(--olive);letter-spacing:.3px}
.social{display:flex;gap:7px}
.social span{width:18px;height:18px;border-radius:50%;background:var(--sage-dark);display:block}
.social span:first-child{background:var(--olive)}
.header-social{left:519px;top:18px}
.main-nav{left:0;top:54px;width:674px;height:30px;background:var(--sage)}
.nav-list{display:flex;align-items:center;font-family:"Cinzel",serif;font-size:8.5px;color:var(--white);letter-spacing:.4px}
.nav-list .on{color:var(--olive)}
.nav-list i{width:4px;height:7px;background:var(--olive);border-radius:50%;margin:0 32px}
.main-nav .nav-list{position:absolute;left:66px;top:11px}
.search{position:absolute;left:542px;top:7px;display:flex;align-items:center;gap:8px;font-family:"Cinzel",serif;font-size:8.5px;color:var(--olive)}
.search svg{display:block}
.hero{left:0;top:84px;width:674px;height:219px;background:linear-gradient(90deg,#eef2f3 0%,#e4ebee 45%,#d5dfe6 70%,#c7d3dc 100%)}
.hero-title{left:63px;top:128px;font-family:"Cinzel",serif;font-weight:600;font-size:21px;line-height:26px;color:var(--ink)}
.hero-text{left:63px;top:182px;width:215px;font-family:Arial,sans-serif;font-size:8.2px;line-height:14.3px;color:var(--ink)}
.btn-read{left:63px;top:236px;width:69px;height:22px;border-radius:11px;background:var(--olive);border:1.5px solid var(--white);box-shadow:0 0 0 1px var(--olive);color:var(--white);font-size:8.5px;display:flex;align-items:center;justify-content:center;font-family:Arial,sans-serif}
.arrow{width:23px;height:23px}
.card{width:215px;height:189px}
.card-photo{position:absolute;inset:0}
.photo-dress{background:linear-gradient(90deg,#7c7873,#8f8b86 50%,#77736e)}
.photo-sky{background:linear-gradient(180deg,#8fb9a6,#c9d49a 55%,#e3dc8e)}
.photo-yoga{background:linear-gradient(180deg,#5b7ea6,#a9b8c8 45%,#6d8aa0 75%,#3f5f55)}
.caption{position:absolute;background:var(--white);font-family:"Cinzel",serif;font-size:10.4px;color:var(--ink);text-align:center;letter-spacing:.3px;line-height:13.5px;display:flex;flex-direction:column;justify-content:center}
.caption.meta{left:27px;top:145px;width:172px;height:44px}
.caption.plain{left:19px;top:152px;width:173px;height:37px}
.btn-view{left:250px;top:960px;width:108px;height:31px;background:var(--olive);color:var(--white);font-family:"Cinzel",serif;font-size:10px;letter-spacing:.5px;display:flex;align-items:center;justify-content:center}
.news-title{left:0;top:1010px;width:674px;text-align:center;font-family:"Cinzel",serif;font-size:21px;color:var(--sage-dark);letter-spacing:.5px}
.news-sub{left:0;top:1036px;width:674px;text-align:center;font-size:7.3px;color:var(--muted)}
.field{top:1061px;width:152px;height:21px;border:1px solid var(--line);border-radius:11px;font-size:6.6px;padding-left:12px;display:flex;align-items:center;font-family:Arial,sans-serif}
.btn-submit{left:461px;top:1061px;width:63px;height:21px;border-radius:11px;background:var(--olive);color:var(--white);font-family:Arial,sans-serif;font-weight:700;font-size:8px;display:flex;align-items:center;justify-content:center}
.footer{left:0;top:1108px;width:674px;height:92px;background:var(--cream)}
.footer .nav-list{position:absolute;left:149px;top:16px;color:var(--ink)}
.footer .nav-list i{margin:0 29px}
.footer-social{left:282px;top:1149px}
.footer-social span{width:20px;height:20px;background:var(--sage-dark)}
.copyright{left:0;top:1184px;width:674px;text-align:center;font-size:7.2px;font-family:Arial,sans-serif;color:var(--ink)}
</style>
</head>
<body>
<div class="abs top-rule"></div>
<div class="abs logo">brightyearsahead.com</div>
<div class="abs social header-social" aria-label="Social links"><span></span><span></span><span></span><span></span></div>

<nav class="abs main-nav">
  <div class="nav-list"><span class="on">Home</span><i></i><span>Fashion</span><i></i><span>Feeling</span><i></i><span>Fitness</span><i></i><span>Contact</span></div>
  <div class="search">SEARCH
    <svg width="18" height="18" viewBox="0 0 18 18"><circle cx="9" cy="9" r="8.3" fill="none" stroke="#a4a03e"/><circle cx="8.4" cy="8.4" r="2.4" fill="none" stroke="#a4a03e" stroke-width="1.1"/><line x1="10.2" y1="10.2" x2="11.8" y2="11.8" stroke="#a4a03e" stroke-width="1.1"/></svg>
  </div>
</nav>

<section class="abs hero" role="img" aria-label="Man in shirt and tie holding a bowl of fresh salad"></section>
<svg class="abs arrow" style="left:20px;top:183px" viewBox="0 0 23 23"><circle cx="11.5" cy="11.5" r="10.8" fill="none" stroke="#fff" stroke-width="1.2"/><path d="M13 8l-3.5 3.5L13 15" fill="none" stroke="#fff" stroke-width="1.2"/></svg>
<svg class="abs arrow" style="left:631px;top:183px" viewBox="0 0 23 23"><circle cx="11.5" cy="11.5" r="10.8" fill="none" stroke="#fff" stroke-width="1.2"/><path d="M10 8l3.5 3.5L10 15" fill="none" stroke="#fff" stroke-width="1.2"/></svg>
<h1 class="abs hero-title">Live Fit Happy &amp;<br>Mindful</h1>
<p class="abs hero-text">Lorem Ipsum is simply dummy text of the printing and typesetting industry. Lorem Ipsum has been the industry's standard dummy text ever since.</p>
<div class="abs btn-read">READ MORE</div>

<article class="abs card" style="left:0;top:330px"><div class="card-photo photo-dress" role="img" aria-label="Woman in a polka dot dress"></div><div class="caption meta"><span>Lorem is the dummy text</span><span>20, May 2018 : Fashion</span></div></article>
<article class="abs card" style="left:228px;top:330px"><div class="card-photo photo-sky" role="img" aria-label="Woman with a rainbow umbrella under a bright sky"></div><div class="caption plain">Lorem is the dummy text</div></article>
<article class="abs card" style="left:457px;top:330px"><div class="card-photo photo-yoga" role="img" aria-label="Woman in a yoga pose above a mountain valley"></div><div class="caption plain">Lorem is the dummy text</div></article>

<article class="abs card" style="left:0;top:536px"><div class="card-photo photo-dress" role="img" aria-label="Woman in a polka dot dress"></div><div class="caption meta"><span>Lorem is the dummy text</span><span>20, May 2018 : Fashion</span></div></article>
<article class="abs card" style="left:228px;top:536px"><div class="card-photo photo-sky" role="img" aria-label="Woman with a rainbow umbrella under a bright sky"></div><div class="caption plain">Lorem is the dummy text</div></article>
<article class="abs card" style="left:457px;top:536px"><div class="card-photo photo-yoga" role="img" aria-label="Woman in a yoga pose above a mountain valley"></div><div class="caption plain">Lorem is the dummy text</div></article>

<article class="abs card" style="left:0;top:742px"><div class="card-photo photo-dress" role="img" aria-label="Woman in a polka dot dress"></div><div class="caption meta"><span>Lorem is the dummy text</span><span>20, May 2018 : Fashion</span></div></article>
<article class="abs card" style="left:228px;top:742px"><div class="card-photo photo-sky" role="img" aria-label="Woman with a rainbow umbrella under a bright sky"></div><div class="caption plain">Lorem is the dummy text</div></article>
<article class="abs card" style="left:457px;top:742px"><div class="card-photo photo-yoga" role="img" aria-label="Woman in a yoga pose above a mountain valley"></div><div class="caption plain">Lorem is the dummy text</div></article>

<div class="abs btn-view">VIEW ALL POSTS</div>

<h2 class="abs news-title">Newsletter Subscription</h2>
<p class="abs news-sub">Subscribe to Our Newsletter to Get Latest Updates &amp; News About Us.</p>
<div class="abs field" style="left:149px">Enter Your Name:</div>
<div class="abs field" style="left:305px">Enter Your Email:</div>
<div class="abs btn-submit">SUBMIT</div>

<footer class="abs footer">
  <div class="nav-list"><span class="on">Home</span><i></i><span>Fashion</span><i></i><span>Feeling</span><i></i><span>Fitness</span><i></i><span>Contact</span></div>
</footer>
<div class="abs social footer-social" aria-label="Social links"><span></span><span></span><span></span><span></span></div>
<p class="abs copyright">© 2018 brightyearsahead.com .All Rights Reserved.</p>
</body>
</html>
```